Business Card Design

Contact Information for Business Card

A vertical business card request- a medium & light gray with silverfern tree logo (logo is attached)

Please use Trebuchet font -- if possible- can we use two different color gray? (See pictures attached below)
Info on the front should be the Silverfern tree logo - on the top of the card, followed by the info ...
Card to read: " " indicated what should be on the card --
Name: " Joan Pelley "
Title : "Partner "
" Office: 202.555.0147 "
" Mobile: 202.555.0182 "

Backside of the card - solid medium color gray color w/ address and small message centered in the card - Trebuchet font
to read:

" 317 B North Linden Avenue, NE "
" Washington, DC 20099 "

Then below address to read:
" Fundraising | Event Planning | Political Consulting "

```html
<!DOCTYPE html>
<html lang="en">
<head>
<meta charset="utf-8">
<title>Silverfern Strategies – Business Card</title>
<link rel="stylesheet" href="https://fonts.googleapis.com/css2?family=Fira+Sans:wght@400;600&family=Questrial&display=swap">
<style>
  :root {
    --charcoal: #3a3f43;
    --silver: #9c9c9c;
    --silver-light: #a8a8a8;
    --mark-tone: #6e7377;
    --paper: #ffffff;
    --ink: #3a3f43;
    --canvas: #ffffff;
  }
  * { margin: 0; padding: 0; box-sizing: border-box; }
  html, body {
    width: 1200px; height: 1200px; overflow: hidden;
    background: var(--canvas);
  }
  .card {
    position: absolute;
    left: 304px;
    width: 602px;
    overflow: hidden;
    box-shadow: 0 0 18px rgba(0,0,0,0.08);
  }
  /* Back of card */
  .card--back {
    top: 239px; height: 344px;
    background: var(--charcoal);
    color: #fff;
    text-align: center;
  }
  .pin {
    position: absolute; left: 286px; top: 118px;
    width: 30px; height: 40px;
  }
  .address {
    position: absolute; left: 0; right: 0; top: 162px;
    font-family: "Fira Sans", "Trebuchet MS", sans-serif;
    font-size: 32px; line-height: 33px; font-weight: 400;
  }
  .services {
    position: absolute; left: 0; right: 0; top: 307px;
    font-family: "Questrial", "Trebuchet MS", sans-serif;
    font-size: 17px; letter-spacing: 0.2px;
  }
  /* Front of card */
  .card--front {
    top: 616px; height: 342px;
    background: var(--paper);
  }
  .swoosh { position: absolute; inset: 0; width: 602px; height: 342px; }
  .person {
    position: absolute; left: 42px; top: 102px;
    font-family: "Fira Sans", "Trebuchet MS", sans-serif;
  }
  .person__name { font-size: 42px; font-weight: 600; color: var(--ink); line-height: 46px; }
  .person__title { font-size: 30px; color: var(--silver-light); line-height: 32px; }
  .contact {
    position: absolute; left: 42px; top: 252px;
    font-family: "Fira Sans", "Trebuchet MS", sans-serif;
    color: var(--ink);
  }
  .contact__email { font-size: 17px; line-height: 24px; margin-bottom: 2px; }
  .contact__phone { font-size: 18px; font-weight: 600; line-height: 21px; }
  .contact__label { color: var(--silver-light); }
  .brand__mark {
    position: absolute; left: 484px; top: 18px;
    width: 92px; height: 92px;
    background: var(--mark-tone);
  }
  .brand__name {
    position: absolute; right: 12px; top: 128px;
    font-family: "Fira Sans", "Trebuchet MS", sans-serif;
    font-size: 20px; font-weight: 400; line-height: 24px;
    color: var(--silver-light);
    text-align: right;
  }
</style>
</head>
<body>
  <section class="card card--back">
    <svg class="pin" viewBox="0 0 30 40" aria-hidden="true">
      <path d="M15 0C6.7 0 0 6.5 0 14.6 0 25 15 40 15 40S30 25 30 14.6C30 6.5 23.3 0 15 0Z" fill="#fff"/>
      <circle cx="15" cy="14.5" r="5.5" fill="var(--charcoal)"/>
    </svg>
    <p class="address">317 B North Linden Avenue, NE<br>Washington, DC 20099</p>
    <p class="services">Fundraising&nbsp; | &nbsp;Event Planning&nbsp; | &nbsp;Political Consulting</p>
  </section>

  <section class="card card--front">
    <svg class="swoosh" viewBox="0 0 602 342" aria-hidden="true">
      <path d="M34,0 C214,2 296,32 334,72 C374,114 394,192 432,250 C472,308 522,336 566,342 L602,342 L602,0 Z" fill="var(--silver)"/>
      <path d="M42,0 C222,0 304,30 344,70 C384,112 404,190 442,248 C480,304 530,334 576,342 L602,342 L602,0 Z" fill="var(--charcoal)"/>
    </svg>
    <div class="person">
      <h1 class="person__name">Joan Pelley</h1>
      <p class="person__title">Partner</p>
    </div>
    <div class="contact">
      <p class="contact__email">joan@silverfernllc.com</p>
      <p class="contact__phone">202.555.0182 <span class="contact__label">mobile</span></p>
      <p class="contact__phone">202.555.0147 <span class="contact__label">office</span></p>
    </div>
    <div class="brand__mark" role="img" aria-label="Company logo symbol area"></div>
    <p class="brand__name">Silverfern Strategies</p>
  </section>
</body>
</html>
```